Packaging Design for Health/Beauty product

This project is for the brand new design of our new product.
Box/Tube/Images
The product is an anesthetic Skin Numbing Cream used for numbing skin for general pain relief and also before tattoos, waxing, laser hair removal and small cosmetic procedures.
Direct to end user and also to salons and studios, with view to selling in pharmacies.
This is a Brand New Product
Packaging design for the brand CALORVEX
2 components -
1. TUBE/OUTER PACKAGING design
and
2. "3D" style graphics/images suitable for marketing
******************
DELIVERABLES:
Tube:
Adobe Illustrator file (.ai) using supplied template for die lines prior to printing/manufacture and PDF files
PNG files for 3D style renderings of front, back, side, and angled left and right.
Outer Packaging:
PNG files for some 3D style renderings of front, back, side, and angled left and right.
******************
WHAT IS THE PRODUCT?
It is an anesthetic skin numbing cream, with Aloe for soothing the skin and Tea Tree
Please google “numbing cream”- images and you’ll get an idea of the 3D styling required.
But - please think “outside the box” and design something that is NOT a copy or modelled off existing brands. We want something completely new to stand out from the crowd without being too "Over The Top."
Keep the core demographic in mind.
This job had previously been given to an artist on here, but prior to completion he ceased replying to my emails. I have a #D image of what we were after.
You may either replicate what was done there (I only have a PDF image, no AI source files) OR you may go for a completely new design.
Both options will be given equal appraisal.
******************
DEMOGRAPHIC
The target market will be for pain relief for injection, vaccinations, waxing, laser hair removal - Mainly for 18-40 year olds, male/female. We also have a view to going into mainstream pharmacies as well.
We are after a visually striking design that will attract the eye and be appealing to our target market- but also a nice clean, uncluttered design.
******************
LOGO INCLUDED - Attachment
Supplied is our "Branding Logo" that is to be incorporated onto both the tube and outer packaging.
IF you have a completely different idea/color scheme that would incorporate a good logo (different than supplied) then that is also ok - it would require you to design the logo as well.
*******************
TEMPLATES - Attachment
2 Templates are supplied - 1 x Tube & 1 x Outer Package
It is for an FDA regulated drug.
The fonts/text on the templates are representative of the WORDING required.
Positioning within each panel can be altered to suit the design, this is for your guidance.
Bar code, NDC code, company logo and other required info will all be supplied.
Please also add a QR code as per the attached example form a different product
Your job is to come up with a great design.
Template provided in Adobe Illustrator (.ai) and must be delivered as same.
*********************
COLORS
Currently we have our logo in green/orange, and we think these neutral colors work well with this market.
As stated, IF you have a totally new idea for LOGO & DESIGN, feel free to use your skills!
Using extra colors comes down to your design, but keep in mind that too many colors can lose impact and not print well.
Remember this will be printed on a plastic tube and a cardboard outer packaging - so the design must be able to look good on a physical product.
Not just on a digital website.
********************
UNIQUE SELLING POINT
Our cream has both Tea Tree & Aloe in the ingredients, and if they can be highlighted in some visual way without detracting from the overall design that would be great.
Use your skills here to represent this as best you can without making it be the main focus.
********************
DRUG FACTS PANEL
Within the supplied templates is a drug facts label that will require some small text changes. WE will make those changes and forward the updated Drug Facts Panel to you.
However the existing panel DIMENSIONS within the template will not change, so you can go ahead and make your design, and we will forward the updated panel asap.
*******************
BARCODE - Attachment
Supplied is a barcode to be used as per template
Please also add a QR Code
******************
NDC CODE - a string of numbers eg/ 12345 678 90
We are still awaiting the receipt of the NDC code, and it may not arrive until after the contest is complete and the winner chosen, and the final adjustments to design made.
Please go ahead and do the main outlay. Upon receipt of the NDC I will send to you for insertion as necessary, wherein the job will be essentially finished.
Then I will need to 2D ai files and PDF templates for submission for registration, AND then also the 3D images that will have the NDC on them, exactly as the package will look once complete.
****************
3D RENDERS
I will need several HIGH QUALITY 3D images for use on our website and in marketing.
Images of the tube (different angles), the box, front and back (different angles), the tube coming out of the opened box, (different angles) - you get the idea what I need.
****************
IMPORTANT
We do not want any photos of people incorporated into the design.
We do not have a blank "3D" style tube for you to use to wrap your label around when creating the promotion style images.
I am awaiting from the manufacturer the final shaping of the tube (it will be similar to the graphic provided) BUT the cap will change shape due to new FDA Rules. Once I have that I will inform you. For now it is ok to use a simple screw cap, but please note that this will need to be changed before final sign off.
Please do your very best to create a great design.
Good luck and may the best design win!
Thankyou very much.

```html
<!DOCTYPE html>
<html lang="en">
<head>
<meta charset="utf-8">
<title>CALORVEX – Lidocaine Cream Packaging</title>
<link href="https://fonts.googleapis.com/css2?family=Cinzel:wght@600&family=Open+Sans:ital,wght@0,400;0,600;0,700;1,400&family=Montserrat:wght@700&display=swap" rel="stylesheet">
<style>
  :root{
    --stage:#2b2b2b;
    --card:#ffffff;
    --panel:#f1f1f1;
    --panel-edge:#dcdcdc;
    --orange:#e8531c;
    --orange-soft:#f08a2c;
    --green:#2f9a2a;
    --green-light:#6cc22e;
    --cap:#5fd41e;
    --ink:#1d1d1d;
    --slot:#3a3a3a;
  }
  *{box-sizing:border-box;margin:0;padding:0}
  html,body{width:1200px;height:1200px;overflow:hidden;background:var(--stage)}
  body{position:relative;font-family:"Open Sans",Arial,sans-serif;color:var(--ink)}

  .brand-dot{display:inline-block;border-radius:50%;background:var(--green);vertical-align:middle;position:relative}

  /* ---------- tube ---------- */
  .tube{position:absolute;left:40px;top:300px;width:240px;height:740px}
  .tube-crimp{position:absolute;left:0;top:0;width:240px;height:14px;background:#e9e9e9;border-bottom:1px solid var(--panel-edge)}
  .tube-body{position:absolute;left:0;top:14px;width:240px;height:616px;background:linear-gradient(90deg,#e8e8e8 0%,#ffffff 35%,#ffffff 70%,#e4e4e4 100%)}
  .tube-cap{position:absolute;left:0;top:630px;width:240px;height:110px;background:linear-gradient(90deg,#46b012 0%,var(--cap) 40%,var(--cap) 70%,#43a80f 100%);border-radius:0 0 14px 14px}
  .tube-vert{position:absolute;writing-mode:vertical-rl;transform:rotate(180deg);white-space:nowrap}
  .tube-brand{left:40px;top:200px;font-family:"Cinzel",serif;font-weight:600;font-size:36px;line-height:44px;color:var(--orange);letter-spacing:1px}
  .tube-brand .brand-dot{width:14px;height:14px;margin-bottom:10px}
  .tube-copy{left:104px;top:150px;font-size:14px;line-height:19px;text-align:center}
  .tube-copy .green{color:var(--green);font-size:15px;font-weight:600}
  .tube-net{left:180px;top:60px;font-size:15px;line-height:20px;color:var(--green)}

  /* ---------- box ---------- */
  .box{position:absolute;left:320px;top:110px;width:840px;height:980px}

  .hang-card{position:absolute;left:0;top:0;width:840px;height:330px;background:var(--card);border-radius:14px 14px 0 0;overflow:hidden}
  .hang-band{position:absolute;left:0;top:0;width:100%;height:84px;background:linear-gradient(90deg,var(--green) 0%,#7aa52a 45%,var(--orange-soft) 100%);color:#fff}
  .hang-slot{position:absolute;left:50%;top:30px;width:160px;height:32px;margin-left:-80px;background:var(--slot);border-radius:16px}
  .band-visit{position:absolute;left:20px;top:14px;font-size:15px;line-height:28px;letter-spacing:.3px}
  .band-visit span{display:block}
  .band-visit span:first-child{padding-left:44px}
  .band-web{position:absolute;right:20px;top:26px;font-size:14px;letter-spacing:.3px}

  .card-brand{position:absolute;left:0;right:0;top:112px;text-align:center;font-family:"Cinzel",serif;font-weight:600;font-size:64px;line-height:1;color:var(--orange);letter-spacing:1px}
  .card-brand .brand-dot{width:20px;height:20px;margin-right:14px;top:-6px}

  .claims{position:absolute;left:18px;top:232px;list-style:none;color:var(--orange);font-size:15px;line-height:21px}
  .card-copy{position:absolute;left:200px;width:440px;top:236px;text-align:center;font-size:17px;line-height:23px}
  .card-copy .lead{font-size:16px}
  .card-copy .green{color:var(--green);font-size:19px}
  .created{position:absolute;right:74px;top:226px;text-align:right;font-size:13px;line-height:18px;font-weight:700;border-right:3px solid var(--orange);padding-right:8px}
  .created .label{color:var(--orange);font-weight:600}
  .leaf-art{position:absolute;right:18px;top:226px;width:46px;height:66px;border-radius:4px;background:linear-gradient(160deg,var(--green-light),var(--green))}

  .top-flap{position:absolute;left:0;top:330px;width:840px;height:90px;background:linear-gradient(180deg,#e6e6e6,var(--panel));border-top:1px solid var(--panel-edge);text-align:center;font-family:"Montserrat",sans-serif;font-weight:700;font-size:14px;letter-spacing:5px;line-height:26px;padding-top:6px}
  .top-flap .l1,.top-flap .l3{color:var(--orange)}
  .top-flap .l2{color:var(--ink)}

  .side-panel{position:absolute;left:0;top:420px;width:140px;height:560px;background:linear-gradient(90deg,#e4e4e4,var(--panel));border-right:1px solid var(--panel-edge)}
  .side-text{position:absolute;left:24px;top:40px;writing-mode:vertical-rl;font-style:italic;color:var(--orange);font-size:17px}
  .side-brand{position:absolute;left:76px;top:130px;writing-mode:vertical-rl;font-family:"Cinzel",serif;font-weight:600;font-size:30px;color:var(--orange);letter-spacing:1px}

  .front-panel{position:absolute;left:140px;top:420px;width:700px;height:560px;overflow:hidden}
  .front-pattern{position:absolute;inset:0;background:radial-gradient(ellipse at 40% 40%,#fafafa 0%,var(--panel) 60%,#e2e2e2 100%)}
  .front-brand{position:absolute;right:40px;top:70px;font-family:"Cinzel",serif;font-weight:600;font-size:66px;line-height:1;color:var(--orange);letter-spacing:1px}
  .front-brand .brand-dot{width:22px;height:22px;margin-right:14px;top:-6px}
  .front-copy{position:absolute;right:40px;width:420px;top:190px;text-align:center;font-size:21px;line-height:30px}
  .front-copy .green{color:var(--green);font-size:22px;font-weight:600}
  .net-wt{position:absolute;right:30px;bottom:50px;font-size:21px;color:var(--green)}
</style>
</head>
<body>

<section class="tube">
  <div class="tube-crimp"></div>
  <div class="tube-body">
    <div class="tube-vert tube-brand"><span class="brand-dot"></span> CALORVEX</div>
    <div class="tube-vert tube-copy">
      <div>4% Lidocaine Cream</div>
      <div class="green">Pain Relieving Topical Anesthetic</div>
      <div>Medicated Cream to Numb The Skin</div>
    </div>
    <div class="tube-vert tube-net">NET WT 2oz (28.4g)</div>
  </div>
  <div class="tube-cap"></div>
</section>

<section class="box">
  <div class="hang-card">
    <div class="hang-band">
      <div class="band-visit"><span>VISIT US@</span><span>WWW.CALORVEX.COM</span></div>
      <div class="hang-slot"></div>
      <div class="band-web">WWW.CALORVEX.COM</div>
    </div>
    <div class="card-brand"><span class="brand-dot"></span>CALORVEX</div>
    <ul class="claims">
      <li>Soothes Sunburn</li>
      <li>Relieves Itch</li>
      <li>Steroid Free</li>
      <li>Goes to Work Fast</li>
    </ul>
    <div class="card-copy">
      <div class="lead">4% Lidocaine Cream</div>
      <div class="green">Pain Relieving Topical Anesthetic</div>
      <div>Medicated Cream to Numb The Skin</div>
    </div>
    <div class="created">
      <div class="label">Created With:</div>
      <div>Aloe</div>
      <div>Tea Tree</div>
      <div>Jojobat</div>
    </div>
    <div class="leaf-art" role="img" aria-label="Green aloe and tea tree leaf illustration"></div>
  </div>

  <div class="top-flap">
    <div class="l1">Works Fast For Rapid Relief</div>
    <div class="l2">Made with Aloe &amp; Tea Tree</div>
    <div class="l3">Numbs The Skin - Safe &amp; Soothing</div>
  </div>

  <div class="side-panel">
    <div class="side-text">4% Lidocaine Caream</div>
    <div class="side-brand">CALORVEX</div>
  </div>

  <div class="front-panel">
    <div class="front-pattern" role="img" aria-label="Faint light grey floral paisley background pattern"></div>
    <div class="front-brand"><span class="brand-dot"></span>CALORVEX</div>
    <div class="front-copy">
      <div>4% Lidocaine Cream</div>
      <div class="green">Pain Relieving Topical Anesthetic</div>
      <div>Medicated Cream to Numb The Skin</div>
    </div>
    <div class="net-wt">NET WT 2oz (28.4g)</div>
  </div>
</section>

</body>
</html>
```